Signage. Will be for store front. Building is on a corner lot. Lots of traffic.

Opening a new location for our landscape business with a garden store (boutique theme) which will have big pottery pots, house plants, ferns and orchids for sale.

And on the side lot of the store we will have bigger bulk items(contractors theme) landscape plants, sod, mulch, soil, rock for sale.

Sign is about 8’x6’

Target Market(s)

Home owners
Landscapers
Builders

Industry/Entity Type

Landscaping

Font styles to use
Sans Serif

Colors
9bcb3c

Requirements
Must have
• “ Installation and Delivery” is a big deal to let people know we do that
Nice to have
• Added a first rendition idea but don’t love it
Added a file with some words to play with
Need help with the words
Should not have
• ?

```html
<!DOCTYPE html>
<html lang="en">
<head>
<meta charset="utf-8">
<title>Fernline Gardens – Storefront Sign</title>
<link rel="stylesheet" href="https://fonts.googleapis.com/css2?family=Barlow+Condensed:wght@600;700&display=swap">
<style>
  :root {
    --backdrop: #b4b5af;
    --sign-white: #ffffff;
    --leaf-green: #7e9a33;
    --deep-green: #667d14;
    --sun-yellow: #ffd000;
    --ink: #161616;
  }
  html, body {
    margin: 0;
    padding: 0;
    width: 1200px;
    height: 1200px;
    overflow: hidden;
    background: var(--backdrop);
  }
  .canvas {
    position: relative;
    width: 1200px;
    height: 1200px;
  }
  .sign {
    position: absolute;
    left: 0;
    top: 150px;
    width: 1200px;
    height: 900px;
    display: block;
  }
  .sign text {
    font-family: "Barlow Condensed", "Arial Narrow", sans-serif;
  }
  .brand-name { fill: var(--leaf-green); font-weight: 700; font-size: 118px; }
  .service-label { fill: var(--ink); font-weight: 700; font-size: 84px; }
  .phone-number { fill: var(--sign-white); font-weight: 700; font-size: 72px; }
  .install-line { fill: var(--deep-green); font-weight: 700; font-size: 114px; }
  .delivery-line { fill: var(--sign-white); font-weight: 700; font-size: 84px; }
  .tick-box { fill: none; stroke: var(--leaf-green); stroke-width: 4; }
  .tick-mark { fill: none; stroke: var(--deep-green); stroke-width: 9; stroke-linecap: round; stroke-linejoin: round; }
</style>
</head>
<body>
<div class="canvas">
  <svg class="sign" viewBox="0 0 1200 900" xmlns="http://www.w3.org/2000/svg" role="img" aria-label="Fernline Gardens storefront sign">
    <rect class="sign-face" x="0" y="0" width="1200" height="900" fill="var(--sign-white)"/>

    <!-- brand block -->
    <g class="brand">
      <text class="brand-name" x="136" y="148" textLength="720" lengthAdjust="spacingAndGlyphs">FERNLINE</text>
      <text class="brand-name" x="136" y="248" textLength="770" lengthAdjust="spacingAndGlyphs">GARDENS</text>
      <circle class="brand-dot" cx="1002" cy="150" r="62" fill="var(--leaf-green)"/>
    </g>

    <!-- services -->
    <g class="services">
      <g class="service-item">
        <rect class="tick-box" x="142" y="356" width="48" height="48" rx="7"/>
        <path class="tick-mark" d="M152 378 L166 392 L196 362"/>
        <text class="service-label" x="219" y="410" textLength="180" lengthAdjust="spacingAndGlyphs">LAWN</text>
      </g>
      <g class="service-item">
        <rect class="tick-box" x="450" y="356" width="48" height="48" rx="7"/>
        <path class="tick-mark" d="M460 378 L474 392 L504 362"/>
        <text class="service-label" x="527" y="410" textLength="532" lengthAdjust="spacingAndGlyphs">GARDEN CENTER</text>
      </g>
      <g class="service-item">
        <rect class="tick-box" x="243" y="463" width="48" height="48" rx="7"/>
        <path class="tick-mark" d="M253 485 L267 499 L297 469"/>
        <text class="service-label" x="323" y="517" textLength="637" lengthAdjust="spacingAndGlyphs">LANDSCAPE DESIGN</text>
      </g>
    </g>

    <!-- bottom bands -->
    <g class="footer-bands">
      <rect class="green-band" x="0" y="652" width="1200" height="248" fill="var(--leaf-green)"/>
      <rect class="band-rule" x="147" y="649" width="1053" height="4" fill="var(--deep-green)"/>
      <polygon class="yellow-band" points="0,655 1108,655 1051,799 0,799" fill="var(--sun-yellow)"/>
      <circle class="corner-disc" cx="56" cy="690" r="140" fill="var(--sun-yellow)" stroke="var(--sign-white)" stroke-width="4"/>
    </g>

    <!-- phone pill -->
    <g class="phone-pill">
      <rect x="265" y="587" width="693" height="94" rx="47" fill="var(--deep-green)"/>
      <circle cx="314" cy="634" r="38" fill="var(--sign-white)"/>
      <path class="phone-icon" fill="var(--deep-green)" d="M300 614 c3 -2 7 -1 8 2 l5 9 c1 3 0 5 -2 7 l-3 2 c2 6 7 11 13 14 l2 -3 c2 -2 5 -3 7 -1 l9 5 c3 2 3 6 1 8 l-4 5 c-3 3 -8 4 -12 2 c-14 -6 -25 -17 -31 -31 c-2 -4 -1 -9 2 -12 z"/>
      <path fill="none" stroke="var(--deep-green)" stroke-width="3" stroke-linecap="round" d="M322 617 a12 12 0 0 1 12 12 M323 608 a21 21 0 0 1 20 20"/>
      <text class="phone-number" x="370" y="660" textLength="560" lengthAdjust="spacingAndGlyphs">(555) 014-2290</text>
    </g>

    <!-- headline -->
    <text class="install-line" x="268" y="782" textLength="708" lengthAdjust="spacingAndGlyphs">INSTALLATION &amp;</text>
    <text class="delivery-line" x="266" y="879" textLength="703" lengthAdjust="spacingAndGlyphs">DELIVERY AVAILABLE</text>
  </svg>
</div>
</body>
</html>
```